Home care agency

Current website QRVCAREPLUS.com. Need to update and reformat to different pages. use my info from my current website

Target Market(s)

adult children

Industry/Entity Type

Home Health

Coding

Coded - Design and coding required

Number of Pages Required

4 page

Font styles to use
Sans Serif

Colors
3276b5
33a6d7
3277b5
85cae6
85acd3

```html
<!DOCTYPE html>
<html lang="en">
<head>
<meta charset="utf-8">
<title>QRV Care Plus — Home</title>
<link rel="stylesheet" href="https://fonts.googleapis.com/css2?family=Oswald:wght@500;600&family=Mr+Dafoe&display=swap">
<style>
  :root {
    --brand-blue: #3276b5;
    --sky-blue: #33a6d7;
    --pale-blue: #85cae6;
    --steel-blue: #85acd3;
    --white: #ffffff;
    --hero-dark: #1c1714;
    --hero-mid: #3a2e27;
    --hero-warm: #4a3a30;
    --page-bg: #f3f3f3;
  }
  * { box-sizing: border-box; margin: 0; padding: 0; }
  html, body {
    width: 1200px;
    height: 800px;
    overflow: hidden;
    background: var(--page-bg);
  }
  .site {
    position: relative;
    width: 1200px;
    height: 800px;
    overflow: hidden;
    font-family: "Oswald", "Arial Narrow", sans-serif;
  }
  .hero {
    position: absolute;
    inset: 0 0 15px 0;
  }
  .hero-photo {
    position: absolute;
    inset: 0;
    background:
      radial-gradient(ellipse 40% 55% at 85% 60%, rgba(120, 105, 95, 0.45), transparent 70%),
      radial-gradient(ellipse 30% 40% at 30% 45%, rgba(110, 95, 80, 0.35), transparent 70%),
      linear-gradient(90deg, #2b2d30 0%, var(--hero-mid) 20%, var(--hero-warm) 50%, var(--hero-mid) 80%, #2f2c2c 100%);
  }
  .hero-shade {
    position: absolute;
    inset: 0;
    background: rgba(10, 8, 6, 0.35);
  }
  .brand-badge {
    position: absolute;
    left: 225px;
    top: 0;
    width: 174px;
    height: 210px;
    background: var(--white);
    border-radius: 0 0 87px 87px;
    display: flex;
    flex-direction: column;
    align-items: center;
    justify-content: center;
    gap: 14px;
    padding-bottom: 10px;
  }
  .brand-mark {
    width: 22px;
    height: 22px;
    border-radius: 50%;
    background: var(--sky-blue);
  }
  .brand-name {
    font-weight: 500;
    font-size: 21px;
    letter-spacing: 1px;
    color: var(--brand-blue);
    text-transform: uppercase;
  }
  .main-nav {
    position: absolute;
    top: 0;
    left: 757px;
    display: flex;
    align-items: flex-start;
  }
  .nav-link {
    display: block;
    height: 59px;
    padding: 22px 0 0;
    margin-right: 30px;
    font-weight: 600;
    font-size: 11px;
    color: var(--white);
    text-decoration: none;
    text-transform: uppercase;
    letter-spacing: 0.1px;
  }
  .nav-link.is-active {
    width: 43px;
    margin-right: 35px;
    text-align: center;
    background: var(--white);
    color: var(--brand-blue);
    border-radius: 0 0 22px 22px;
  }
  .hero-copy {
    position: absolute;
    left: 0;
    right: 0;
    top: 372px;
    text-align: center;
    color: var(--white);
  }
  .hero-script {
    font-family: "Mr Dafoe", cursive;
    font-weight: 400;
    font-size: 62px;
    line-height: 1;
  }
  .hero-title {
    font-weight: 600;
    font-size: 45px;
    line-height: 1.1;
    margin-top: 6px;
    letter-spacing: -0.5px;
  }
  .hero-button {
    display: inline-block;
    margin-top: 16px;
    width: 105px;
    height: 36px;
    line-height: 34px;
    border: 1px solid rgba(255, 255, 255, 0.8);
    border-radius: 2px;
    font-weight: 600;
    font-size: 13px;
    letter-spacing: 2px;
    color: var(--white);
    text-decoration: none;
    text-transform: uppercase;
  }
  .accent-bar {
    position: absolute;
    left: 0;
    right: 0;
    bottom: 0;
    height: 15px;
    background: var(--brand-blue);
  }
</style>
</head>
<body>
  <div class="site">
    <section class="hero">
      <div class="hero-photo" role="img" aria-label="Photo of a caregiver in a white coat standing beside a seated older man in a warmly lit living room with a table lamp"></div>
      <div class="hero-shade"></div>

      <a class="brand-badge" href="#" aria-label="QRV Care Plus home">
        <span class="brand-mark"></span>
        <span class="brand-name">QRV Care Plus</span>
      </a>

      <nav class="main-nav">
        <a class="nav-link is-active" href="#">Home</a>
        <a class="nav-link" href="#">About Us</a>
        <a class="nav-link" href="#">Services</a>
        <a class="nav-link" href="#">Contact</a>
      </nav>

      <div class="hero-copy">
        <p class="hero-script">Providing Care</p>
        <h1 class="hero-title">Throughout the South Shore</h1>
        <a class="hero-button" href="#">Learn More</a>
      </div>
    </section>
    <div class="accent-bar"></div>
  </div>
</body>
</html>
```